Global Weight loss program

we need a business card based in Brooklyn , NY called PeppertonRUN . Mara Dulvik Tenbrook the founder and creator of PeppertonRUN Movement. A business based around nutrition, health, Whole Foods and fitness.

Industry/Entity Type

Food Service

Contact Information for Business Card

Phone number : 718-555-0143
website www.peppertonrun.com
email : mara@peppertonrun.com

Font styles to use
Sans Serif

Requirements
Must have
• logo colors
• green black and gold
Nice to have
• must be simple and sharp.
Should not have
• pictures of items

```html
<!DOCTYPE html>
<html lang="en">
<head>
<meta charset="utf-8">
<title>PeppertonRUN Business Card</title>
<link href="https://fonts.googleapis.com/css2?family=Roboto:wght@400;500;700&display=swap" rel="stylesheet">
<style>
  :root {
    --canvas-bg: #e9e6e1;
    --card-dark: #262828;
    --card-light: #f4f4f2;
    --brand-green: #5cb82e;
    --ink-dark: #2e2f30;
    --ink-muted: #8a8c8c;
    --ink-white: #f2f2f2;
  }
  * { box-sizing: border-box; margin: 0; padding: 0; }
  html, body { width: 1200px; height: 911px; overflow: hidden; }
  body {
    background: var(--canvas-bg);
    font-family: "Roboto", Arial, sans-serif;
    position: relative;
  }
  .card {
    position: absolute;
    top: 167px;
    width: 330px;
    height: 577px;
    box-shadow: 0 10px 30px rgba(0,0,0,0.22);
    display: flex;
    flex-direction: column;
    align-items: center;
  }
  .card--back { left: 215px; background: var(--card-dark); }
  .card--front { left: 655px; background: var(--card-light); }

  /* back side */
  .back-brand {
    margin-top: 218px;
    display: flex;
    align-items: center;
    gap: 8px;
    color: var(--ink-white);
    font-weight: 700;
    font-size: 20px;
  }
  .brand-square { width: 16px; height: 16px; background: var(--brand-green); }
  .person-name {
    margin-top: 18px;
    color: var(--brand-green);
    font-weight: 700;
    font-size: 20px;
  }
  .person-role {
    margin-top: 3px;
    color: var(--ink-white);
    font-weight: 500;
    font-size: 13px;
    letter-spacing: 0.5px;
  }
  .divider {
    margin: 14px 0 12px;
    width: 22px;
    height: 1px;
    background: var(--brand-green);
  }
  .contact {
    color: var(--ink-white);
    font-size: 13px;
    line-height: 19px;
    text-align: center;
  }
  .contact .web {
    color: var(--brand-green);
    font-weight: 500;
    letter-spacing: 1.5px;
  }

  /* front side */
  .front-brand {
    margin-top: 230px;
    display: flex;
    align-items: center;
    gap: 10px;
    color: var(--ink-dark);
    font-weight: 700;
    font-size: 34px;
    letter-spacing: -0.5px;
  }
  .front-brand .brand-square { width: 24px; height: 24px; }
  .tagline {
    margin-top: 4px;
    color: var(--ink-muted);
    font-size: 9px;
    letter-spacing: 2.4px;
  }
  .services {
    margin-top: auto;
    margin-bottom: 84px;
    color: var(--ink-dark);
    font-weight: 500;
    font-size: 12px;
    line-height: 16px;
    text-align: center;
  }
</style>
</head>
<body>
  <section class="card card--back" aria-label="Card back">
    <div class="back-brand"><span class="brand-square"></span>PeppertonRUN</div>
    <h1 class="person-name">Mara Dulvik Tenbrook</h1>
    <p class="person-role">FOUNDER</p>
    <div class="divider"></div>
    <p class="contact">
      718-555-0143<br>
      mara@peppertonrun.com<br>
      <span class="web">www.peppertonrun.com</span>
    </p>
  </section>

  <section class="card card--front" aria-label="Card front">
    <div class="front-brand"><span class="brand-square"></span>PeppertonRUN</div>
    <p class="tagline">Fitness, Nutrition and Health</p>
    <p class="services">Health Coach | Personal Trainer<br>Natural Gourmet Chef</p>
  </section>
</body>
</html>
```